1 postcard flyer for Car Camcorder 2sided FULL COLOR$$$$$$$$

3.5x5.5 inches front and back Full Color
side1 (1 solid color background, portrait layout)
(on the top heading Bold/Stands out) ACCIDENT PROTECTION (Below this on the left side)
Staged Accidents
Crash for Cash
Accident Blames (these three are bad, evil, monstrous things)
(on the right side, a warrior is Standing tall wiith a strong body, instead of a head of man, use a camera lens as head, holding a sword and Shield)(The Shield will have these words written on it and make sure these words are easy to read) Car Camcorder will Protect You from scams

(at the bottom of side1 the footer)
Car Camcorder is your Witness & DOESN'T LIE!

(if anyone has a better design idea to relate the message on the flyer about Car Camcorder will Protect You from scams, please go ahead make your own with the same message that car camcorder will protect you from scams like staged accidents, crash for cash, accident blames)(side1 must be 1 solid color background, portrait layout)

Side2 (whatever solid or multiple color background design of your choice is fine)( a fine looking girl featuring the Car Camcorder functions, the girl picture DOES NOT need to be sexy or showing cleavage, just attractive is good)
What is a Car Camcorder?
Records Video While Driving
Continuous Loop Recording
Easy Installation as a GPS
Auto-On&Off by Cigarette Plug
Impact Detected, Video Clip Will Lock
Car Camcorder will provide You Peace of Mind
(side 2 please leave room for me to stick a 1 inch height label at the bottom)
(also somewhere on this side please add a round or square dot "Starting $60, so reader will know how much car camcorder will cost. I don't want to put any pictures of my car camcorder on the flyer.)

Target Market(s)

Everyone that drives a Vehicle.

Industry/Entity Type

Camera

Requirements
Must have
• Please following the provided template and make sure the design is set per template's instructions. Both sides must be design with 350dpi and CMYK.

```html
<!DOCTYPE html>
<html lang="en">
<head>
<meta charset="utf-8">
<title>What is a Car Camcorder? – Postcard Side 2</title>
<link rel="stylesheet" href="https://fonts.googleapis.com/css2?family=Bevan&family=Federant&display=swap">
<style>
  :root {
    --backdrop: #d6d4d2;
    --brand-red: #c2391d;
    --panel-yellow: #fde07c;
    --feature-red: #c0361b;
    --ink-dark: #2b2622;
    --title-gold-top: #fbe6a2;
    --title-gold-bottom: #d8962e;
    --title-outline: #5a2a12;
    --badge-brown-light: #8a5a45;
    --badge-brown-dark: #4d2d22;
    --badge-text: #f6d9a8;
    --photo-light: #e7c6a6;
    --photo-mid: #c9a27c;
    --photo-dark: #9a9b9c;
  }
  * { margin: 0; padding: 0; box-sizing: border-box; }
  html, body {
    width: 1200px; height: 900px; overflow: hidden;
    background: var(--backdrop);
  }
  .postcard {
    position: absolute; left: 50px; top: 100px;
    width: 1100px; height: 700px;
    background: var(--panel-yellow);
    overflow: hidden;
    box-shadow: 0 6px 18px rgba(0,0,0,0.25);
  }
  .header-band {
    position: absolute; left: 0; top: 0;
    width: 1100px; height: 124px;
    background: var(--brand-red);
  }
  .side-band {
    position: absolute; left: 0; top: 0;
    width: 240px; height: 700px;
    background: var(--brand-red);
  }
  .headline {
    position: absolute; right: 36px; top: 28px;
    font-family: "Bevan", serif;
    font-size: 50px; line-height: 1;
    letter-spacing: 0.5px;
    background: linear-gradient(to bottom, var(--title-gold-top), var(--title-gold-bottom));
    -webkit-background-clip: text; background-clip: text;
    color: transparent;
    -webkit-text-stroke: 1.5px var(--title-outline);
    filter: drop-shadow(2px 3px 0 rgba(60,20,5,0.6));
    white-space: nowrap;
  }
  .model-photo {
    position: absolute; left: 36px; top: 60px;
    width: 240px; height: 640px;
    border-radius: 110px 110px 0 0;
    background: linear-gradient(to bottom, var(--photo-light) 0%, var(--photo-mid) 38%, var(--photo-dark) 62%, #b7b8b9 100%);
  }
  .price-badge {
    position: absolute; left: 318px; top: 170px;
    width: 220px; height: 220px;
  }
  .feature-list {
    position: absolute; right: 32px; top: 140px;
    list-style: none;
    text-align: right;
  }
  .feature {
    display: flex; align-items: center; justify-content: flex-end;
    gap: 14px;
    height: 78px;
    font-family: "Federant", cursive;
    font-size: 35px;
    color: var(--feature-red);
    white-space: nowrap;
  }
  .feature svg { width: 40px; height: 38px; flex: none; }
  .tagline {
    position: absolute; right: 32px; top: 538px;
    font-family: "Federant", cursive;
    font-size: 33px;
    font-weight: 700;
    color: var(--ink-dark);
    white-space: nowrap;
    -webkit-text-stroke: 0.6px var(--ink-dark);
  }
</style>
</head>
<body>
  <main class="postcard">
    <div class="side-band"></div>
    <div class="header-band"></div>
    <h1 class="headline">What is a Car Camcorder?</h1>

    <div class="model-photo" role="img" aria-label="Photo of a smiling young woman with long blond hair in a grey hoodie, pointing at the price badge"></div>

    <svg class="price-badge" viewBox="0 0 224 224" role="img" aria-label="Starting $60">
      <defs>
        <radialGradient id="badgeFill" cx="45%" cy="40%" r="65%">
          <stop offset="0" stop-color="#8a5a45"/>
          <stop offset="1" stop-color="#4d2d22"/>
        </radialGradient>
      </defs>
      <circle cx="112" cy="112" r="110" fill="url(#badgeFill)"/>
      <circle cx="112" cy="112" r="99" fill="none" stroke="#e8d2b8" stroke-width="7" stroke-dasharray="2 3"/>
      <g transform="rotate(-22 112 112)" font-family="Federant, cursive" fill="#f6d9a8" stroke="#3a1e14" stroke-width="1.5" paint-order="stroke" text-anchor="middle">
        <text x="110" y="104" font-size="38">Starting</text>
        <text x="112" y="152" font-size="48">$60</text>
      </g>
    </svg>

    <ul class="feature-list">
      <li class="feature">
        <svg viewBox="0 0 40 38"><rect x="2" y="8" width="28" height="28" fill="none" stroke="#c0361b" stroke-width="3"/><path d="M8 20 L16 29 L36 3" fill="none" stroke="#c0361b" stroke-width="5" stroke-linecap="round" stroke-linejoin="round"/></svg>
        Records Video While Driving
      </li>
      <li class="feature">
        <svg viewBox="0 0 40 38"><rect x="2" y="8" width="28" height="28" fill="none" stroke="#c0361b" stroke-width="3"/><path d="M8 20 L16 29 L36 3" fill="none" stroke="#c0361b" stroke-width="5" stroke-linecap="round" stroke-linejoin="round"/></svg>
        Continuous Loop Recording
      </li>
      <li class="feature">
        <svg viewBox="0 0 40 38"><rect x="2" y="8" width="28" height="28" fill="none" stroke="#c0361b" stroke-width="3"/><path d="M8 20 L16 29 L36 3" fill="none" stroke="#c0361b" stroke-width="5" stroke-linecap="round" stroke-linejoin="round"/></svg>
        Easy Installation as a GPS
      </li>
      <li class="feature">
        <svg viewBox="0 0 40 38"><rect x="2" y="8" width="28" height="28" fill="none" stroke="#c0361b" stroke-width="3"/><path d="M8 20 L16 29 L36 3" fill="none" stroke="#c0361b" stroke-width="5" stroke-linecap="round" stroke-linejoin="round"/></svg>
        Auto-On&amp;Off by Cigarette Plug
      </li>
      <li class="feature">
        <svg viewBox="0 0 40 38"><rect x="2" y="8" width="28" height="28" fill="none" stroke="#c0361b" stroke-width="3"/><path d="M8 20 L16 29 L36 3" fill="none" stroke="#c0361b" stroke-width="5" stroke-linecap="round" stroke-linejoin="round"/></svg>
        Impact Detected, Video Clip Will Lock
      </li>
    </ul>

    <p class="tagline">Car Camcorder will provide You Peace of Mind</p>
  </main>
</body>
</html>
```